TRB Fitouts

Kitchen installations/ carpentry / labour hire

Target Market(s)

Building companys

Industry/Entity Type

Carpentry

Contact Information for Business Card

Director Jordan Example
Phone no 0491 570 156
Email jordan@trbfitouts.example.com.au

Requirements
Nice to have
• A finished kitchen on one side in the background I would like my company name in big writing and my name in small writing so on one side I would like trb fitouts and on the other side have my details with the picture of the kitchen in the back round
Should not have
• Fork and spoons

```html
<!DOCTYPE html>
<html lang="en">
<head>
<meta charset="utf-8">
<title>TRB Fitouts – Business Card</title>
<link rel="stylesheet" href="https://fonts.googleapis.com/css2?family=Cinzel:wght@400;600&family=Open+Sans:wght@400&display=swap">
<style>
  :root {
    --backdrop: #d9d9db;
    --teal: #23959a;
    --card-white: #ffffff;
    --ink: #3a3a3a;
    --faint: #efefef;
    --shadow: rgba(0, 0, 0, 0.18);
  }
  * { margin: 0; padding: 0; box-sizing: border-box; }
  html, body {
    width: 1200px;
    height: 900px;
    overflow: hidden;
    background: var(--backdrop);
  }
  .stage { position: relative; width: 1200px; height: 900px; }
  .card {
    position: absolute;
    width: 560px;
    height: 320px;
    border-radius: 28px;
    overflow: hidden;
    box-shadow: 0 10px 24px var(--shadow);
  }
  .card-front {
    left: 110px;
    top: 120px;
    background: var(--teal);
    display: flex;
    align-items: center;
    justify-content: center;
  }
  .brand-name {
    font-family: "Cinzel", serif;
    font-weight: 600;
    line-height: 1;
  }
  .card-front .brand-name { color: var(--card-white); text-align: center; }
  .brand-main { display: block; font-size: 76px; letter-spacing: 4px; }
  .brand-sub { display: block; font-size: 30px; letter-spacing: 6px; margin-top: 6px; }

  .card-back { left: 530px; top: 460px; background: var(--card-white); }
  .back-decoration {
    position: absolute;
    right: 40px;
    top: 30px;
    width: 230px;
    height: 230px;
    background: var(--faint);
  }
  .card-back .brand-name {
    position: absolute;
    left: 34px;
    top: 40px;
    color: var(--teal);
    text-align: left;
  }
  .card-back .brand-main { font-size: 62px; letter-spacing: 3px; }
  .card-back .brand-sub { font-size: 26px; letter-spacing: 5px; margin-top: 2px; }

  .holder {
    position: absolute;
    left: 34px;
    top: 160px;
    font-family: "Open Sans", sans-serif;
  }
  .holder-name {
    font-family: "Cinzel", serif;
    font-weight: 400;
    color: var(--teal);
    font-size: 20px;
    letter-spacing: 1px;
  }
  .holder-role { font-size: 14px; color: var(--ink); margin-top: -2px; }
  .contact-list {
    list-style: none;
    margin-top: 12px;
    font-size: 14px;
    color: var(--ink);
  }
  .contact-list li {
    display: flex;
    align-items: center;
    gap: 7px;
    line-height: 21px;
  }
  .contact-icon { width: 12px; height: 12px; flex: none; }

  .address {
    position: absolute;
    right: 30px;
    top: 178px;
    text-align: right;
    font-family: "Open Sans", sans-serif;
    font-size: 13px;
    line-height: 19px;
    color: var(--ink);
  }
</style>
</head>
<body>
<main class="stage">
  <section class="card card-front" aria-label="Card front">
    <p class="brand-name"><span class="brand-main">TRB</span><span class="brand-sub">FITOUTS</span></p>
  </section>

  <section class="card card-back" aria-label="Card back">
    <div class="back-decoration" aria-hidden="true"></div>
    <p class="brand-name"><span class="brand-main">TRB</span><span class="brand-sub">FITOUTS</span></p>

    <div class="holder">
      <p class="holder-name">JORDAN EXAMPLE</p>
      <p class="holder-role">Managing Director</p>
      <ul class="contact-list">
        <li>
          <svg class="contact-icon" viewBox="0 0 12 12" aria-hidden="true"><path d="M1 4 Q6 0 11 4 L9 5 L8 4 L4 4 L3 5 Z M3 6 L9 6 L10 11 L2 11 Z" fill="var(--teal)"/></svg>
          0491 570 156
        </li>
        <li>
          <svg class="contact-icon" viewBox="0 0 12 12" aria-hidden="true"><rect x="3" y="0.5" width="6" height="11" rx="1.2" fill="none" stroke="var(--teal)" stroke-width="1.4"/><rect x="4.3" y="2" width="3.4" height="6" fill="var(--teal)"/></svg>
          0491 570 157
        </li>
        <li>
          <svg class="contact-icon" viewBox="0 0 12 12" aria-hidden="true"><rect x="0.5" y="2.5" width="11" height="7.5" fill="var(--teal)"/><path d="M0.5 2.5 L6 7 L11.5 2.5" fill="none" stroke="#fff" stroke-width="1"/></svg>
          jordan@trbfitouts.example.com.au
        </li>
      </ul>
    </div>

    <p class="address">12345, Address Goes Here<br>Country Name, 123456</p>
  </section>
</main>
</body>
</html>
```